Boulder Grip Supply Business Card Design Challenge

Please create me a simple card using my logo. I'm not looking for anything abstract.
A couple of colours for text and maybe something on the card so the whole card isn't just a white board.
Please send me samples and I'll reply with suggestions to refine the design. Thank you

Reason: The Ormeau address was incorrect in the brief, so I have updated that so the 4 and 5 star submissions can be updated and resubmitted please!!! Sorry and thank you

Target Market(s)

Mining companies and rock producing aggregate companies. Quarries

Industry/Entity Type

Mining

Contact Information for Business Card

Name - Graham Ellsworth / Company Logo AND Boulder Grip Supply Pty Ltd / position - Managing Director / address1 - Unit 3, 14 Tindal Crescent, Kelridge 4299 Queensland AU / address2 - PO Box 917, Marlow Vale 4297 Queensland AU / mobile - 0427 915 306 / phone - 07 5591 4867 / fax - 07 5591 4803 / email - ge@bouldergripsupply.example.au / website - www.bouldergripsupply.example.au

Requirements
Must have
• Business details as per the above. The phone and fax numbers will be confirmed before the end of the project. Thank you
• SINGLE SIDED ONLY please on Card, not transparent plastic

```html
<!DOCTYPE html>
<html lang="en">
<head>
<meta charset="utf-8">
<title>Boulder Grip Supply – Business Card</title>
<link href="https://fonts.googleapis.com/css2?family=Lato:wght@400;700;900&display=swap" rel="stylesheet">
<style>
  :root {
    --backdrop: #e9e6e1;
    --card: #ffffff;
    --ink: #4a4a4c;
    --ink-soft: #5c5c5e;
    --accent: #29a8df;
  }
  * { margin: 0; padding: 0; box-sizing: border-box; }
  html, body {
    width: 1200px; height: 600px; overflow: hidden;
    background: var(--backdrop);
    font-family: "Lato", Arial, sans-serif;
  }
  .card {
    position: absolute; left: 180px; top: 60px;
    width: 840px; height: 480px;
    background: var(--card);
    box-shadow: 0 6px 24px rgba(0,0,0,0.12);
  }
  .brand {
    position: absolute; left: 60px; top: 150px; width: 320px;
    display: flex; align-items: center; gap: 14px;
  }
  .brand-mark { width: 44px; height: 44px; background: var(--accent); flex: none; }
  .brand-name {
    font-weight: 900; font-size: 30px; line-height: 1.05;
    color: var(--ink); text-transform: uppercase; letter-spacing: 0.5px;
  }
  .divider {
    position: absolute; left: 410px; top: 60px;
    width: 2px; height: 250px; background: var(--accent);
  }
  .person { position: absolute; left: 440px; top: 62px; }
  .person-name { font-weight: 700; font-size: 30px; color: var(--accent); }
  .person-title { font-size: 22px; color: var(--ink-soft); margin-top: 2px; }
  .contacts { position: absolute; left: 440px; top: 160px; list-style: none; }
  .contacts li {
    display: flex; align-items: center; gap: 10px;
    font-size: 20px; color: var(--ink-soft); height: 30px;
  }
  .contacts svg { width: 16px; height: 16px; flex: none; fill: var(--ink); }
  .addresses {
    position: absolute; left: 100px; top: 370px;
    font-size: 21px; color: var(--ink-soft); line-height: 34px;
  }
</style>
</head>
<body>
  <div class="card">
    <div class="brand">
      <span class="brand-mark"></span>
      <span class="brand-name">Boulder Grip Supply</span>
    </div>

    <div class="divider"></div>

    <div class="person">
      <div class="person-name">Graham Ellsworth</div>
      <div class="person-title">Managing Director</div>
    </div>

    <ul class="contacts">
      <li>
        <svg viewBox="0 0 16 16" aria-label="mobile"><path d="M4 1h8v14H4z M5.5 2.5v10h5v-10z" fill-rule="evenodd"/></svg>
        0427 915 306
      </li>
      <li>
        <svg viewBox="0 0 16 16" aria-label="phone"><path d="M1 5c0-2 2-3 7-3s7 1 7 3v2h-4V5H5v2H1z M3 8h10l1 6H2z"/></svg>
        07 5591 4867
      </li>
      <li>
        <svg viewBox="0 0 16 16" aria-label="fax"><path d="M4 1h8v5H4z M1 7h14v8H1z"/></svg>
        07 5591 4803
      </li>
      <li>
        <svg viewBox="0 0 16 16" aria-label="email"><path d="M1 3h14v10H1z M2 4l6 5 6-5"/></svg>
        ge@bouldergripsupply.example.au
      </li>
      <li>
        <svg viewBox="0 0 16 16" aria-label="website"><circle cx="8" cy="8" r="7"/><path d="M1 8h14M8 1v14" stroke="#fff" stroke-width="1.2"/></svg>
        www.bouldergripsupply.example.au
      </li>
    </ul>

    <div class="addresses">
      <div>address1 - Unit 3, 14 Tindal Crescent, Kelridge 4299 Queensland AU</div>
      <div>address2 - PO Box 917, Marlow Vale 4297 Queensland AU</div>
    </div>
  </div>
</body>
</html>
```